We are in search of a new business card design for our business. We have a Mexican Grocery Store called Tortilla Grove Market, we would like to see that some have mexican design, but we are open to any type of designs.

Phone: to be announced
Fax: to be announced

Address is:
2415 Calloway Blvd
Linden Park, MD 21499

```html
<!DOCTYPE html>
<html lang="en">
<head>
<meta charset="utf-8">
<title>Tortilla Grove Market – Business Card</title>
<link rel="stylesheet" href="https://fonts.googleapis.com/css2?family=Lobster&family=Montserrat:wght@500;600&display=swap">
<style>
  :root {
    --page-bg: #e9e6e1;
    --card-yellow: #f9bd1f;
    --card-yellow-deep: #f3ad12;
    --panel-line: #1a1a1a;
    --brand-red: #c8281e;
    --ink-navy: #2c3552;
  }
  * { margin: 0; padding: 0; box-sizing: border-box; }
  html, body { width: 1200px; height: 1000px; overflow: hidden; }
  body {
    background: var(--page-bg);
    position: relative;
    font-family: "Montserrat", Arial, sans-serif;
  }
  .card {
    position: absolute;
    left: 220px;
    width: 760px;
    height: 434px;
    background: linear-gradient(135deg, var(--card-yellow) 0%, var(--card-yellow-deep) 100%);
    box-shadow: 0 6px 18px rgba(0,0,0,0.18);
    overflow: hidden;
  }
  .card-front { top: 50px; }
  .card-back { top: 516px; }
  .panel-lines { position: absolute; inset: 0; width: 100%; height: 100%; }
  .panel-lines line, .panel-lines polygon {
    stroke: var(--panel-line); stroke-width: 2; fill: none;
  }
  .brand-mark {
    position: absolute;
    display: flex;
    align-items: center;
    gap: 6px;
    font-family: "Lobster", Georgia, cursive;
    color: var(--brand-red);
    white-space: nowrap;
    transform: translate(-50%, -50%);
  }
  .brand-dot {
    border-radius: 50%;
    background: var(--brand-red);
    flex: none;
  }
  .brand-mark-large {
    left: 380px; top: 217px;
    font-size: 48px; line-height: 1.05;
    text-align: center;
    gap: 12px;
  }
  .brand-mark-large .brand-dot { width: 24px; height: 24px; }
  .brand-mark-small { font-size: 14px; }
  .brand-mark-small .brand-dot { width: 9px; height: 9px; }
  .mark-top { left: 380px; top: 38px; }
  .mark-bottom { left: 380px; top: 396px; }
  .mark-left { left: 92px; top: 217px; }
  .mark-right { left: 668px; top: 217px; }
  .contact {
    position: absolute;
    left: 380px; top: 217px;
    transform: translate(-50%, -50%);
    color: var(--ink-navy);
    font-style: normal;
    white-space: nowrap;
  }
  .contact-name {
    font-family: "Lobster", Georgia, cursive;
    color: var(--brand-red);
    font-size: 24px;
    font-weight: 400;
    margin-bottom: 6px;
  }
  .contact-line {
    font-size: 17px;
    font-weight: 600;
    line-height: 1.35;
  }
  .contact-phone { margin-top: 6px; font-weight: 500; }
  .contact-phone b { font-weight: 600; }
</style>
</head>
<body>

<section class="card card-front" aria-label="Card front">
  <svg class="panel-lines" viewBox="0 0 760 434" aria-hidden="true">
    <polygon points="190,217 280,80 480,80 570,217 480,354 280,354"/>
    <line x1="280" y1="80" x2="0" y2="0"/>
    <line x1="480" y1="80" x2="760" y2="0"/>
    <line x1="280" y1="354" x2="0" y2="434"/>
    <line x1="480" y1="354" x2="760" y2="434"/>
  </svg>
  <div class="brand-mark brand-mark-large">
    <span class="brand-dot"></span>
    <span>Tortilla Grove<br>Market</span>
  </div>
</section>

<section class="card card-back" aria-label="Card back">
  <svg class="panel-lines" viewBox="0 0 760 434" aria-hidden="true">
    <polygon points="190,217 280,80 480,80 570,217 480,354 280,354"/>
    <line x1="280" y1="80" x2="0" y2="0"/>
    <line x1="480" y1="80" x2="760" y2="0"/>
    <line x1="280" y1="354" x2="0" y2="434"/>
    <line x1="480" y1="354" x2="760" y2="434"/>
  </svg>

  <div class="brand-mark brand-mark-small mark-top"><span class="brand-dot"></span>Tortilla Grove Market</div>
  <div class="brand-mark brand-mark-small mark-bottom"><span class="brand-dot"></span>Tortilla Grove Market</div>
  <div class="brand-mark brand-mark-small mark-left"><span class="brand-dot"></span>Tortilla Grove</div>
  <div class="brand-mark brand-mark-small mark-right"><span class="brand-dot"></span>Tortilla Grove</div>

  <address class="contact">
    <p class="contact-name">Tortilla Grove Market</p>
    <p class="contact-line">2415 Calloway Blvd.</p>
    <p class="contact-line">Linden Park, MD 21499</p>
    <p class="contact-line contact-phone"><b>P:</b> +(0) 555 201480</p>
    <p class="contact-line contact-phone"><b>Fax:</b> +(0) 555 201481</p>
  </address>
</section>

</body>
</html>
```